Letterhead and Stationary for Construction Company

Brisk Current needs modern Letterhead, Envelopes and Notepad designs.

Industry/Entity Type

Construction

Colors
f78f20
34a7d8
ffffff

Requirements
Must have
• Modern looking design.

```html
<!DOCTYPE html>
<html lang="en">
<head>
<meta charset="utf-8">
<title>Brisk Current — Stationery Set</title>
<link href="https://fonts.googleapis.com/css2?family=Figtree:wght@400;600&display=swap" rel="stylesheet">
<style>
  :root {
    --backdrop: #d0d0d0;
    --paper: #f0f0f0;
    --brand-blue: #006db3;
    --brand-blue-dark: #0062a2;
    --brand-orange: #f07014;
    --ink: #3a3a3a;
  }
  html, body {
    margin: 0;
    padding: 0;
    width: 1200px;
    height: 1041px;
    overflow: hidden;
    background: var(--backdrop);
    font-family: "Figtree", Arial, sans-serif;
  }
  .stage { position: relative; width: 1200px; height: 1041px; }
  .piece {
    position: absolute;
    background: var(--paper);
    box-shadow: 0 1px 2px rgba(0,0,0,0.18);
    overflow: hidden;
  }
  .piece svg.art { position: absolute; left: 0; top: 0; }

  .brand-lockup {
    position: absolute;
    display: flex;
    align-items: center;
    gap: 8px;
  }
  .brand-dot {
    border-radius: 50%;
    border-style: solid;
    border-color: var(--brand-orange);
    box-sizing: border-box;
    flex: none;
  }
  .brand-name {
    color: var(--brand-blue);
    font-weight: 600;
    line-height: 0.95;
    letter-spacing: -0.01em;
  }

  /* Presentation folder */
  .folder { left: 166px; top: 130px; width: 417px; height: 541px; border-radius: 3px; }
  .folder .brand-lockup { left: 180px; top: 424px; gap: 10px; }
  .folder .brand-dot { width: 54px; height: 54px; border-width: 5px; }
  .folder .brand-name { font-size: 33px; }

  /* Letterhead */
  .letterhead { left: 615px; top: 150px; width: 403px; height: 522px; }
  .letterhead .brand-lockup { left: 31px; top: 24px; }
  .letterhead .brand-dot { width: 32px; height: 32px; border-width: 3px; }
  .letterhead .brand-name { font-size: 18px; }
  .contact-list {
    position: absolute;
    left: 302px;
    top: 22px;
    margin: 0;
    padding: 0;
    list-style: none;
    font-size: 5.4px;
    line-height: 7px;
    color: var(--ink);
  }
  .contact-list li { display: flex; align-items: center; gap: 3px; }
  .contact-list svg { width: 5px; height: 5px; fill: var(--brand-blue); }
  .contact-address { margin-top: 3px; font-size: 5.4px; line-height: 7px; color: var(--ink); }

  /* Envelope front */
  .envelope-front { left: 132px; top: 698px; width: 451px; height: 197px; }
  .envelope-front .brand-lockup { left: 18px; top: 23px; }
  .envelope-front .brand-dot { width: 32px; height: 32px; border-width: 3px; }
  .envelope-front .brand-name { font-size: 18px; }
  .return-address {
    position: absolute;
    left: 26px;
    top: 169px;
    font-size: 5.4px;
    line-height: 7px;
    color: var(--ink);
  }
  .return-marker { position: absolute; left: 18px; top: 171px; }

  /* Envelope back */
  .envelope-back { left: 615px; top: 698px; width: 451px; height: 197px; }
  .flap-name {
    position: absolute;
    left: 0; right: 0;
    top: 26px;
    text-align: center;
    color: var(--paper);
    font-weight: 600;
    font-size: 12px;
  }
</style>
</head>
<body>
<main class="stage">

  <section class="piece folder" aria-label="Presentation folder">
    <svg class="art" width="417" height="541" viewBox="0 0 417 541">
      <rect width="417" height="541" fill="var(--brand-blue)"/>
      <path d="M0,452 Q210,315 417,254 L417,541 L0,541 Z" fill="var(--brand-orange)"/>
      <path d="M0,459 Q220,332 417,280 L417,541 L0,541 Z" fill="var(--paper)"/>
      <rect x="0" y="0" width="27" height="541" fill="#000" opacity="0.04"/>
      <line x1="27" y1="0" x2="27" y2="541" stroke="#000" stroke-opacity="0.12"/>
      <line x1="2" y1="0" x2="2" y2="541" stroke="#fff" stroke-opacity="0.15"/>
    </svg>
    <div class="brand-lockup">
      <span class="brand-dot"></span>
      <span class="brand-name">Brisk<br>Current</span>
    </div>
  </section>

  <section class="piece letterhead" aria-label="Letterhead">
    <svg class="art" width="403" height="522" viewBox="0 0 403 522">
      <path d="M137,522 Q310,505 403,425 L403,522 Z" fill="var(--brand-orange)"/>
      <path d="M209,522 Q330,500 403,437 L403,522 Z" fill="var(--brand-blue)"/>
    </svg>
    <div class="brand-lockup">
      <span class="brand-dot"></span>
      <span class="brand-name">Brisk<br>Current</span>
    </div>
    <ul class="contact-list">
      <li><svg viewBox="0 0 10 10"><path d="M2,1 L4,1 L5,3 L4,4 Q5,6 6,6 L7,5 L9,6 L9,8 Q5,9 2,5 Q1,3 2,1Z"/></svg>305-555-0148</li>
      <li><svg viewBox="0 0 10 10"><rect x="1" y="3" width="8" height="5"/><rect x="3" y="1" width="4" height="2"/></svg>877-555-0192</li>
      <li><svg viewBox="0 0 10 10"><rect x="1" y="2" width="8" height="6"/></svg>info@briskcurrent.com</li>
      <li><svg viewBox="0 0 10 10"><circle cx="5" cy="5" r="4"/></svg>www.briskcurrent.com</li>
      <li class="contact-address">2150 Harbor View Dr.<br>Suite 310, Bayside Point</li>
    </ul>
  </section>

  <section class="piece envelope-front" aria-label="Envelope front">
    <svg class="art" width="451" height="197" viewBox="0 0 451 197">
      <path d="M188,197 Q370,180 451,102 L451,197 Z" fill="var(--brand-orange)"/>
      <path d="M264,197 Q390,175 451,112 L451,197 Z" fill="var(--brand-blue)"/>
    </svg>
    <div class="brand-lockup">
      <span class="brand-dot"></span>
      <span class="brand-name">Brisk<br>Current</span>
    </div>
    <svg class="return-marker" width="5" height="11" viewBox="0 0 5 11"><path d="M0,0 L5,5.5 L0,11 Z" fill="#b5b5b5"/></svg>
    <p class="return-address" style="margin:0">2150 Harbor View Dr.<br>Suite 310, Bayside Point</p>
  </section>

  <section class="piece envelope-back" aria-label="Envelope back">
    <svg class="art" width="451" height="197" viewBox="0 0 451 197">
      <path d="M0,0 L451,0 L435,66 L17,66 Z" fill="var(--brand-blue)"/>
      <line x1="17" y1="66.5" x2="435" y2="66.5" stroke="#000" stroke-opacity="0.1"/>
    </svg>
    <div class="flap-name">Brisk Current</div>
  </section>

</main>
</body>
</html>
```